When the boots match march on! book cover design

Book cover for a business, non-fiction book.
About stepping up, being who you truly are, and willing not to fit in.

TITLE: When The Boots Match, March On!
SUBTITLE: Quit copying the chief others expect of you and begin shaping the chief nobody else could ever shape...
AUTHOR: Tobias Hartwell-Brenner
Updates

we never uploaded the brief

Target Market(s)

Business people, curious leaders, insiders who have a secret itch to be an outsider
AGE: 35-50 years old

Font styles to use
Sans Serif
Other font styles liked:
• designer's choice!

Requirements
Must have
• Very visual
Imagery must reflect the topic of the book

```html
<!DOCTYPE html>
<html lang="en">
<head>
<meta charset="utf-8">
<title>When The Boots Match, March On! — Book Cover</title>
<link rel="stylesheet" href="https://fonts.googleapis.com/css2?family=League+Spartan:wght@700;800&display=swap">
<style>
  :root {
    --paper: #ffffff;
    --ink: #0d0d0d;
    --cape-light: #e8102a;
    --cape-mid: #c60d22;
    --cape-dark: #950616;
    --suit: #6d6d6d;
    --title: #ffffff;
  }
  html, body {
    margin: 0;
    padding: 0;
    overflow: hidden;
    background: var(--paper);
  }
  .cover {
    position: relative;
    width: 800px;
    height: 1200px;
    overflow: hidden;
    background: var(--paper);
    font-family: "League Spartan", sans-serif;
  }
  .hero-figure {
    position: absolute;
    left: 0;
    top: 0;
  }
  .tagline {
    position: absolute;
    left: 66px;
    top: 62px;
    width: 262px;
    margin: 0;
    font-weight: 800;
    font-size: 16.5px;
    line-height: 24px;
    letter-spacing: -0.3px;
    text-transform: uppercase;
    color: var(--ink);
  }
  .title {
    position: absolute;
    left: 205px;
    top: 272px;
    width: 420px;
    margin: 0;
    text-align: center;
    font-weight: 800;
    font-size: 96px;
    line-height: 105px;
    letter-spacing: -3px;
    text-transform: uppercase;
    color: var(--title);
  }
  .title span { display: block; }
  .author {
    position: absolute;
    right: 63px;
    top: 1128px;
    margin: 0;
    font-weight: 800;
    font-size: 25px;
    letter-spacing: -0.8px;
    text-transform: uppercase;
    color: var(--ink);
    white-space: nowrap;
  }
</style>
</head>
<body>
<main class="cover">
  <svg class="hero-figure" width="800" height="1200" viewBox="0 0 800 1200"
       role="img" aria-label="Photograph of a businessman in a grey suit and glasses seen from behind, hands on hips, wearing a long red superhero cape">
    <defs>
      <linearGradient id="capeTone" x1="0" y1="0" x2="1" y2="1">
        <stop offset="0" stop-color="var(--cape-light)"/>
        <stop offset="0.55" stop-color="var(--cape-mid)"/>
        <stop offset="1" stop-color="var(--cape-dark)"/>
      </linearGradient>
    </defs>
    <rect x="190" y="185" width="440" height="830" rx="60" fill="url(#capeTone)"/>
  </svg>

  <p class="tagline">Quit copying the chief others expect of you and begin shaping the chief nobody else could ever shape...</p>

  <h1 class="title">
    <span>When</span>
    <span>The</span>
    <span>Boots</span>
    <span>Match,</span>
    <span>March</span>
    <span>On!</span>
  </h1>

  <p class="author">Tobias Hartwell-Brenner</p>
</main>
</body>
</html>
```